Toravel Project Consulting

I need a logo and business card design for a small business operating in the management consulting and contractor space, predominantly in local and state government. I specialise in project management, financial consulting, people and culture, procurement, ICT transformation and contracting for corporate support areas of organisations.

Industry/Entity Type

Business

```html
<!DOCTYPE html>
<html lang="en">
<head>
<meta charset="utf-8">
<title>Toravel Project Consulting – Business Card</title>
<link rel="stylesheet" href="https://fonts.googleapis.com/css2?family=Open+Sans:wght@400;600;700&display=swap">
<style>
  :root {
    --backdrop: #2a2b2f;
    --card-white: #ffffff;
    --brand-orange: #ff6200;
    --ink-dark: #1d1d1d;
    --ink-grey: #6b6b6b;
    --text-light: #ffffff;
  }
  * { margin: 0; padding: 0; box-sizing: border-box; }
  html, body {
    width: 1200px;
    height: 864px;
    overflow: hidden;
    background: var(--backdrop);
    font-family: "Open Sans", sans-serif;
  }
  .stage {
    position: relative;
    width: 1200px;
    height: 864px;
  }
  .card {
    position: absolute;
    width: 580px;
    height: 332px;
    border-radius: 3px;
    box-shadow: 0 14px 30px rgba(0,0,0,0.45);
  }
  .card-front {
    left: 310px;
    top: 56px;
    background: var(--card-white);
    display: flex;
    flex-direction: column;
    align-items: center;
    justify-content: center;
    gap: 34px;
  }
  .card-back {
    left: 310px;
    top: 446px;
    background: var(--brand-orange);
    color: var(--text-light);
    text-align: center;
    padding-top: 52px;
  }
  .brand-lockup {
    display: flex;
    align-items: center;
    gap: 14px;
  }
  .brand-dot {
    width: 44px;
    height: 44px;
    border-radius: 50%;
    background: var(--brand-orange);
  }
  .brand-name {
    font-size: 30px;
    font-weight: 400;
    color: var(--brand-orange);
    letter-spacing: 0.2px;
  }
  .service-list {
    text-align: center;
    font-size: 14.5px;
    font-weight: 700;
    color: var(--ink-dark);
    line-height: 1.45;
  }
  .service-sep {
    display: inline-block;
    width: 7px;
    height: 7px;
    border-radius: 50%;
    background: var(--brand-orange);
    margin: 0 10px;
    vertical-align: middle;
  }
  .holder-name {
    font-size: 20px;
    font-weight: 700;
  }
  .holder-role {
    font-size: 13.5px;
    margin-top: -2px;
  }
  .holder-address {
    font-size: 15px;
    line-height: 1.45;
    margin-top: 22px;
  }
  .holder-contact {
    font-size: 15px;
    line-height: 1.45;
    margin-top: 22px;
  }
  .holder-contact strong { font-weight: 700; }
</style>
</head>
<body>
<main class="stage">
  <section class="card card-front" aria-label="Card front">
    <div class="brand-lockup">
      <span class="brand-dot"></span>
      <span class="brand-name">Toravel Project Consulting</span>
    </div>
    <p class="service-list">
      Project management<span class="service-sep"></span>Financial consulting<br>
      People and culture<span class="service-sep"></span>Procurement<br>
      ICT transformation and<br>
      Contracting for corporate support areas of organisations.
    </p>
  </section>

  <section class="card card-back" aria-label="Card back">
    <p class="holder-name">Daniel Reeve</p>
    <p class="holder-role">Director</p>
    <p class="holder-address">14 Harlow Parade<br>Westbury NSW 2071</p>
    <p class="holder-contact">
      <strong>Phone:</strong> 0491570156<br>
      <strong>Email:</strong> info@toravelproject.com<br>
      <strong>Website:</strong> www.toravelproject.com
    </p>
  </section>
</main>
</body>
</html>
```